Help me create an amazing cover for my first ebook!!

I am looking to have a modern and professional looking cover for my first ebook. It will be published through Borvex Quill Self Press and will need to follow their formatting and guidelines. I want the cover to have a modern and vibrant feel, that appeals to a millennial audience. This is a real estate book that is focused on a niche category catered to young professionals, so the idea would be to appeal to them.

Title:
The Twentysomething Playbook for Duplex Living

A Smart Property Buying Plan to Start Early, Cut Your Housing Costs (Sometimes to Zero), and Speed Up Your Path to Lasting Wealth.

Davin Osterlund

Target Market(s)

Real Estate investors, investors, millennials, young professionals, college educated, 20-40 years old.Financial freedom, finance.

Industry/Entity Type

Real Estate

Font styles to use
Sans Serif

Colors

Designer to choose colors to be used in the design.

Requirements
Must have
• Must follow the borvex quill self press format. I attached a screenshot of the details, it can also be found here: https://qsp.borvexbooks.example/en_US/help/topic/R481736025
• Must include this title:
• The Twentysomething Playbook for Duplex Living
• A Smart Property Buying Plan to Start Early, Cut Your Housing Costs (Sometimes to Zero), and Speed Up Your Path to Lasting Wealth.
• Davin Osterlund.
• I added examples of book covers I like to use as a guide, I also added some color pallette examples.
Nice to have
• Modern, clean design that's not too busy. Some sort of simple photo or illustration to incorporate in the cover along with the text would be nice.

```html
<!DOCTYPE html>
<html lang="en">
<head>
<meta charset="utf-8">
<title>The Twentysomething Playbook for Duplex Living — Davin Osterlund</title>
<link rel="stylesheet" href="https://fonts.googleapis.com/css2?family=Montserrat:wght@400;600;800;900&display=swap">
<style>
  :root {
    --paper: #ffffff;
    --crimson: #9c1238;
    --indigo: #5a5db6;
    --sky: #a9e3ef;
    --snow: #ffffff;
    --sketch-light: #f1f2f4;
    --sketch-mid: #d9dbe0;
    --sketch-edge: #b9bcc4;
  }
  html, body {
    margin: 0;
    padding: 0;
    width: 752px;
    height: 1200px;
    overflow: hidden;
    background: var(--paper);
  }
  .cover {
    position: relative;
    width: 752px;
    height: 1200px;
    overflow: hidden;
    font-family: "Montserrat", sans-serif;
    background: var(--paper);
  }
  .backdrop {
    position: absolute;
    inset: 0;
    width: 752px;
    height: 1200px;
  }
  .band-top { fill: var(--crimson); }
  .band-bottom { fill: var(--indigo); }
  .author {
    position: absolute;
    top: 32px;
    left: 0;
    width: 752px;
    margin: 0;
    text-align: center;
    color: var(--snow);
    font-weight: 600;
    font-size: 27px;
    letter-spacing: 6px;
  }
  .house-art {
    position: absolute;
    left: 110px;
    top: 140px;
    width: 520px;
    height: 470px;
    clip-path: polygon(30% 0, 62% 8%, 100% 30%, 96% 100%, 10% 100%, 0 40%);
    background: radial-gradient(ellipse at 50% 45%, var(--sketch-light) 0%, var(--sketch-mid) 70%, var(--sketch-edge) 100%);
  }
  .title {
    position: absolute;
    left: 0;
    top: 632px;
    width: 752px;
    margin: 0;
    text-align: center;
    font-weight: 800;
    line-height: 1;
  }
  .title span { display: block; }
  .title-lead {
    color: var(--sky);
    font-size: 42px;
    letter-spacing: 1px;
  }
  .title-main {
    color: var(--snow);
    font-weight: 900;
    font-size: 104px;
    letter-spacing: -2px;
    margin-top: 10px;
  }
  .title-joiner {
    color: var(--snow);
    font-size: 32px;
    margin-top: 6px;
  }
  .title-tail {
    color: var(--sky);
    font-size: 58px;
    letter-spacing: 1px;
    margin-top: 2px;
  }
  .subtitle {
    position: absolute;
    left: 76px;
    top: 948px;
    width: 600px;
    margin: 0;
    text-align: center;
    color: var(--snow);
    font-weight: 600;
    font-size: 27px;
    line-height: 1.4;
    text-transform: uppercase;
  }
</style>
</head>
<body>
<main class="cover">
  <svg class="backdrop" viewBox="0 0 752 1200" aria-hidden="true">
    <polygon class="band-top" points="0,0 752,0 752,95 0,305"/>
    <polygon class="band-bottom" points="0,470 752,290 752,1200 0,1200"/>
  </svg>

  <p class="author">DAVIN OSTERLUND</p>

  <div class="house-art" role="img" aria-label="Line sketch of a two-storey modern house with a gabled roof and wraparound balconies"></div>

  <h1 class="title">
    <span class="title-lead">THE TWENTYSOMETHING</span>
    <span class="title-main">PLAYBOOK</span>
    <span class="title-joiner">for</span>
    <span class="title-tail">DUPLEX LIVING</span>
  </h1>

  <p class="subtitle">A Smart Property Buying Plan to Start Early, Cut Your Housing Costs (Sometimes to Zero), and Speed Up Your Path to Lasting Wealth.</p>
</main>
</body>
</html>
```